We need a set of stationary to compliment our new logo including letterhead (A4 & A5), envelopes, Business cards and appointment cards.

Hi Designers - our details are set out below.
Ashbrook Family Medical
Shop 7, 23-25 Tolley Parade
GAWLER EAST SA 5118
Phone - 08 84967342
Fax - 08 84967349
www.ashbrookfm-example.com.au

Cheers Meg

Industry/Entity Type

Medical

Requirements
Must have
• Reflect the logo be modern and classy

```html
<!DOCTYPE html>
<html lang="en">
<head>
<meta charset="utf-8">
<title>Ashbrook Family Medical – Stationery Set</title>
<link href="https://fonts.googleapis.com/css2?family=Quicksand:wght@400;500;600&display=swap" rel="stylesheet">
<style>
:root{
  --backdrop:#343434;
  --paper:#ffffff;
  --paper-soft:#f1f1f1;
  --leaf:#8cbf44;
  --sky:#5279bd;
  --ink:#3c3c3c;
  --muted:#8a8a8a;
  --rule:#b9b9b9;
}
*{box-sizing:border-box;margin:0;padding:0}
html,body{width:1200px;height:880px;overflow:hidden}
body{background:var(--backdrop);font-family:"Quicksand",sans-serif;color:var(--ink);position:relative}
.sheet{position:absolute;background:var(--paper);overflow:hidden}
.brand{color:var(--sky);font-weight:500;text-transform:uppercase;line-height:1.05;text-align:center}
.brand-dot{display:block;border-radius:50%;background:var(--leaf);margin:0 auto}

/* Letterhead */
.letterhead{left:74px;top:100px;width:326px;height:442px}
.lh-sender{position:absolute;left:22px;top:18px;width:190px;border-bottom:1px solid var(--rule);padding-bottom:4px}
.lh-name{font-size:9px;font-weight:600}
.lh-addr{font-size:6px;font-style:italic;color:var(--muted);line-height:1.35}
.lh-web{position:absolute;left:22px;top:54px;font-size:7.5px;color:var(--sky)}
.lh-brand{position:absolute;left:244px;top:16px;width:76px}
.lh-brand .brand-dot{width:18px;height:18px;margin-bottom:3px}
.lh-brand .brand{font-size:10px}
.lh-brand .brand small{display:block;font-size:5px;letter-spacing:1px}
.lh-watermark{position:absolute;left:90px;top:222px;width:170px;height:170px;border-radius:50%;background:var(--leaf);opacity:.18}
.lh-body{position:absolute;left:62px;top:110px;width:228px;font-size:7.2px;line-height:1.22;text-align:justify;color:#222}
.lh-body p{text-indent:12px;margin-bottom:7px}
.lh-sign{position:absolute;left:236px;top:354px;font-size:8px}
.lh-signature{position:absolute;left:240px;top:368px;width:44px;height:12px;background:linear-gradient(90deg,#cfcfcf,#9a9a9a);opacity:.5;border-radius:6px}
.lh-footer{position:absolute;left:4px;right:4px;top:410px;font-size:8px;display:flex;justify-content:space-between;white-space:nowrap}
.lh-footer b,.lh-email b{font-weight:500;color:var(--leaf)}
.lh-email{position:absolute;left:115px;top:428px;font-size:8px}

/* Cards */
.card{width:132px;height:74px}
.card::before,.card::after{content:"";position:absolute;top:14px;width:46px;height:46px;border-radius:50%}
.card::before{left:-24px;background:var(--leaf)}
.card::after{right:-24px;background:var(--sky)}
.card-front .brand-dot{width:13px;height:13px;margin-top:6px}
.card-front .brand{font-size:8.5px;margin-top:2px}
.card-front .brand small{display:block;font-size:3.5px;letter-spacing:.8px}
.card-person{text-align:center;font-size:5.5px;margin-top:8px}
.card-person span{display:block;font-size:4.5px;color:var(--muted);font-style:italic}
.card-appt .brand-dot{width:8px;height:8px;margin-top:4px}
.card-appt .brand{font-size:5.5px;margin-top:1px}
.appt-fields{position:relative;margin:4px 28px 0 28px;font-size:5px;color:var(--muted);line-height:1.6}
.appt-fields div{border-bottom:.5px solid var(--rule)}
.appt-fields .pair{display:flex;gap:6px;border:0}
.appt-fields .pair span{flex:1;border-bottom:.5px solid var(--rule)}
.appt-contact{position:absolute;left:0;right:0;top:58px;font-size:3px;text-align:center;line-height:1.35;color:#555}

/* Folder */
.folder{left:770px;top:100px;width:338px;height:462px;background:var(--paper-soft)}
.folder-band{position:absolute;left:276px;top:0;width:2px;height:100%;background:var(--sky)}
.folder-brand{position:absolute;left:30px;top:136px;width:280px}
.folder-brand .brand-dot{width:88px;height:88px;margin-bottom:16px}
.folder-brand .brand{font-size:44px;letter-spacing:-.5px}
.folder-brand .brand small{display:block;text-align:right;font-size:9px;letter-spacing:4px;margin-top:2px}

/* Envelopes */
.envelope{height:160px;background:var(--paper-soft)}
.env-front{left:80px;top:618px;width:314px}
.env-front .env-brand{position:absolute;left:4px;top:6px;width:90px}
.env-brand .brand-dot{width:22px;height:22px;margin-bottom:4px}
.env-brand .brand{font-size:13px}
.env-brand .brand small{display:block;font-size:4px;letter-spacing:1.2px}
.env-stamp{position:absolute;left:270px;top:10px;width:22px;height:28px;background:linear-gradient(135deg,#b49a7d,#7a6550)}
.env-address{position:absolute;left:110px;top:70px;font-size:11px;font-style:italic;line-height:1.45;color:#555}
.env-back{left:428px;top:616px;width:318px}
.env-back .flap{position:absolute;left:0;top:0;width:100%;height:40px}
.env-back .env-brand{position:absolute;left:119px;top:66px;width:80px}
.env-back .brand-dot{width:40px;height:40px}
</style>
</head>
<body>

<section class="sheet letterhead" aria-label="Letterhead">
  <div class="lh-sender">
    <p class="lh-name">Alex Reed</p>
    <p class="lh-addr">Tolley Parade 23<br>5118 Gawler East, Australia</p>
  </div>
  <p class="lh-web">www.ashbrookfm-example.com.au</p>
  <div class="lh-brand">
    <span class="brand-dot"></span>
    <p class="brand">Ashbrook<small>Family Medical</small></p>
  </div>
  <div class="lh-watermark"></div>
  <div class="lh-body">
    <p>Lorem ipsum dolor sit amet, consectetuer adipiscing elit, sed diam nonummy nibh euismod tincidunt ut laoreet dolore magna aliquam erat volutpat. Ut wisi enim ad minim veniam, quis nostrud exerci tation ullamcorper suscipit lobortis nisl ut aliquip ex ea commodo consequat.</p>
    <p>Duis autem vel eum iriure dolor in hendrerit in vulputate velit esse molestie consequat, vel illum dolore eu feugiat nulla facilisis at vero eros et accumsan et iusto odio dignissim qui blandit praesent luptatum zzril delenit augue duis dolore te feugait nulla facilisi. Nam liber tempor cum soluta nobis eleifend option congue nihil imperdiet doming id quod mazim placerat facer possim assum. Typi non habent claritatem insitam; est usus legentis in iis qui facit eorum claritatem.</p>
    <p>Investigationes demonstraverunt lectores legere me lius quod ii legunt saepius. Claritas est etiam processus dynamicus, qui sequitur mutationem consuetudium lectorum. Mirum est notare quam littera gothica, quam nunc putamus parum claram, anteposuerit litterarum formas humanitatis per seacula quarta decima et quinta decima. Eodem modo typi, qui nunc nobis videntur parum clari, fiant sollemnes in futurum.</p>
  </div>
  <p class="lh-sign">Alex Reed</p>
  <div class="lh-signature" role="img" aria-label="Handwritten signature"></div>
  <div class="lh-footer">
    <span><b>PHONE</b> 08 84967342</span>
    <span><b>FAX</b> 08 84967349</span>
    <span><b>MOBILE</b> 0400 555 018</span>
  </div>
  <p class="lh-email"><b>EMAIL</b> hello@ashbrook-example.com</p>
</section>

<section class="sheet card card-front" style="left:426px;top:476px" aria-label="Business card">
  <span class="brand-dot"></span>
  <p class="brand">Ashbrook<small>Family Medical</small></p>
  <p class="card-person">Alex Reed<span>medical doctor</span></p>
</section>

<section class="sheet card card-appt" style="left:614px;top:476px" aria-label="Appointment card">
  <span class="brand-dot"></span>
  <p class="brand">Ashbrook Family Medical</p>
  <div class="appt-fields">
    <div>NAME:</div>
    <div class="pair"><span>DATE:</span><span>TIME:</span></div>
  </div>
  <p class="appt-contact">PHONE 08 84967342 FAX 08 84967349<br>EMAIL hello@ashbrook-example.com WEB ashbrookfm-example.com.au<br>ADDRESS Shop 7, 23-25 Tolley Parade</p>
</section>

<section class="sheet folder" aria-label="Presentation folder">
  <div class="folder-band"></div>
  <div class="folder-brand">
    <span class="brand-dot"></span>
    <p class="brand">Ashbrook<small>Family Medical</small></p>
  </div>
</section>

<section class="sheet envelope env-front" aria-label="Envelope front">
  <div class="env-brand">
    <span class="brand-dot"></span>
    <p class="brand">Ashbrook<small>Family Medical</small></p>
  </div>
  <div class="env-stamp" role="img" aria-label="Postage stamp"></div>
  <p class="env-address">Ashbrook Family Medical<br>Tolley Parade 23,<br>5118 Gawler East, Australia</p>
</section>

<section class="sheet envelope env-back" aria-label="Envelope back">
  <svg class="flap" viewBox="0 0 318 40" preserveAspectRatio="none"><path d="M0 0 L6 36 L312 36 L318 0" fill="none" stroke="#c8c8c8" stroke-width="1"/></svg>
  <div class="env-brand"><span class="brand-dot"></span></div>
</section>

<section class="sheet card card-front" style="left:772px;top:616px" aria-label="Business card">
  <span class="brand-dot"></span>
  <p class="brand">Ashbrook<small>Family Medical</small></p>
  <p class="card-person">Alex Reed<span>medical doctor</span></p>
</section>

<section class="sheet card card-appt" style="left:960px;top:616px" aria-label="Appointment card">
  <span class="brand-dot"></span>
  <p class="brand">Ashbrook Family Medical</p>
  <div class="appt-fields">
    <div>NAME:</div>
    <div class="pair"><span>DATE:</span><span>TIME:</span></div>
  </div>
  <p class="appt-contact">PHONE 08 84967342 FAX 08 84967349<br>EMAIL hello@ashbrook-example.com WEB ashbrookfm-example.com.au<br>ADDRESS Shop 7, 23-25 Tolley Parade</p>
</section>

</body>
</html>
```